Indoor Air Restoration company needs graphic design for a 6x12 v nose trailer to wrap

We offer mold services, duct cleaning, water damage clean up and odor removal. "We find, fix and prevent mold, odor and allergen problems" is what we want to communicate on this trailer, which is a rolling billboard. We like the blue and orange color themes, as found in our logo. The company name is Bright Nest Partners and the logo is attached below. We'd like to see our message clearly, company name and what we offer. We tend to lean towards white letters on a darker background (blue or orange) but are very open to outside ideas, as we are stuck! Our website is available for reference if that is helpful. www.brightnestpro.com The phone number to be printed on truck is 302-555-0148, Happy designing!!

Target Market(s)

Home owners

Industry/Entity Type

Indoor Air Quality, Mold Remediation

Font styles to use
Sans Serif

Colors
0054AA
0677BA
7BADD7
CADEEF
E8F1F8
F0912C
F2A743
F7CA91
FBE8D2
FDF5EE

Requirements
Must have
• our message, company name and phone
Nice to have
• services we offer (mold remediation, duct cleaning, water damage and odor removal
Should not have
• cartoon feel

```html
<!DOCTYPE html>
<html lang="en">
<head>
<meta charset="utf-8">
<title>Bright Nest Partners – Trailer Wrap</title>
<link href="https://fonts.googleapis.com/css2?family=Montserrat:wght@800;900&family=Roboto+Condensed:wght@500;700&display=swap" rel="stylesheet">
<style>
  :root {
    --blue-deep: #0054AA;
    --blue: #1580C4;
    --blue-mid: #0677BA;
    --orange: #F07427;
    --orange-soft: #F5884A;
    --white: #FFFFFF;
    --ink: #000000;
  }
  html, body {
    margin: 0;
    padding: 0;
    width: 1200px;
    height: 599px;
    overflow: hidden;
    background: var(--white);
  }
  .wrap {
    position: relative;
    width: 1200px;
    height: 599px;
    overflow: hidden;
    font-family: "Montserrat", Arial, sans-serif;
  }
  .backdrop {
    position: absolute;
    inset: 0;
  }
  .brand-name {
    position: absolute;
    left: 38px;
    top: 118px;
    width: 250px;
    text-align: center;
    font-family: "Roboto Condensed", Arial, sans-serif;
    font-weight: 700;
    font-size: 36px;
    line-height: 38px;
    letter-spacing: 1px;
    color: var(--blue-deep);
    text-transform: uppercase;
  }
  .headline {
    position: absolute;
    margin: 0;
    font-family: "Montserrat", Arial, sans-serif;
    font-weight: 900;
    line-height: 1;
    transform-origin: left top;
    white-space: nowrap;
  }
  .headline-we {
    left: 314px;
    top: 210px;
    font-size: 128px;
    letter-spacing: -4px;
    color: var(--white);
    transform: scaleX(0.87);
  }
  .headline-offer {
    left: 360px;
    top: 298px;
    font-size: 100px;
    letter-spacing: -3px;
    color: var(--orange-soft);
    transform: scaleX(0.88);
  }
  .headline-dots {
    position: absolute;
    left: 670px;
    top: 346px;
    display: flex;
    gap: 7px;
  }
  .headline-dots span {
    width: 17px;
    height: 17px;
    border-radius: 50%;
    background: var(--white);
  }
  .tagline {
    position: absolute;
    margin: 0;
    font-family: "Roboto Condensed", Arial, sans-serif;
    font-weight: 700;
    font-size: 27px;
    line-height: 34px;
    color: var(--white);
    white-space: nowrap;
  }
  .tagline-1 { left: 167px; top: 393px; }
  .tagline-2 { left: 254px; top: 427px; }
  .phone {
    position: absolute;
    left: 61px;
    top: 482px;
    width: 367px;
    height: 76px;
    border: 4px solid var(--white);
    border-radius: 28px;
  }
  .phone-icon {
    position: absolute;
    left: 38px;
    top: 494px;
    width: 56px;
    height: 56px;
  }
  .phone-number {
    position: absolute;
    left: 102px;
    top: 489px;
    margin: 0;
    font-family: "Roboto Condensed", Arial, sans-serif;
    font-weight: 700;
    font-size: 54px;
    line-height: 60px;
    letter-spacing: 1px;
    color: var(--white);
    white-space: nowrap;
  }
  .service {
    position: absolute;
    width: 238px;
    margin: 0;
    text-align: center;
    font-family: "Montserrat", Arial, sans-serif;
    font-weight: 900;
    font-size: 40px;
    line-height: 38px;
    color: var(--ink);
  }
  .service-water { left: 698px; top: 208px; }
  .service-mold  { left: 894px; top: 95px; }
  .service-odor  { left: 898px; top: 320px; }
  .service-duct  { left: 696px; top: 436px; }
</style>
</head>
<body>
<div class="wrap">
  <svg class="backdrop" width="1200" height="599" viewBox="0 0 1200 599" aria-hidden="true">
    <defs>
      <linearGradient id="bg-sweep" x1="0" y1="0" x2="1" y2="0">
        <stop offset="0" stop-color="#1580C4"/>
        <stop offset="0.42" stop-color="#1580C4"/>
        <stop offset="0.62" stop-color="#7A7C9A"/>
        <stop offset="0.82" stop-color="#C4785A"/>
        <stop offset="1" stop-color="#F07427"/>
      </linearGradient>
      <linearGradient id="hex-rim" x1="0" y1="0" x2="1" y2="0">
        <stop offset="0" stop-color="#1580C4"/>
        <stop offset="1" stop-color="#F07427"/>
      </linearGradient>
    </defs>
    <rect class="bg" width="1200" height="599" fill="url(#bg-sweep)"/>

    <g class="bubbles" fill="#FFFFFF">
      <circle cx="280" cy="212" r="110" opacity="0.1"/>
      <circle cx="510" cy="322" r="221" opacity="0.1"/>
      <circle cx="620" cy="110" r="49" opacity="0.18"/>
      <circle cx="1107" cy="540" r="49" opacity="0.18"/>
    </g>

    <polygon class="brand-banner" points="38,0 288,0 288,190 163,260 38,190" fill="#FFFFFF"/>

    <g class="hexes" fill="#FFFFFF" stroke="#FFFFFF" stroke-width="30" stroke-linejoin="round">
      <polygon points="1108,243 1160,133 1215,133 1215,353 1160,353"/>
      <polygon points="909,130 961,36 1065,36 1117,130 1065,223 961,223"/>
      <polygon points="913,360 965,267 1069,267 1121,360 1069,452 965,452"/>
      <polygon points="711,472 763,378 867,378 919,472 867,565 763,565"/>
    </g>
    <polygon class="hex-rim" points="709,243 761,148 869,148 921,243 869,337 761,337"
             fill="none" stroke="url(#hex-rim)" stroke-width="36" stroke-linejoin="round"/>
    <polygon class="hex-featured" points="711,243 763,150 867,150 919,243 867,335 763,335"
             fill="#FFFFFF" stroke="#FFFFFF" stroke-width="28" stroke-linejoin="round"/>
  </svg>

  <div class="brand-name">Bright Nest<br>Partners</div>

  <h1 class="headline headline-we">WE</h1>
  <h1 class="headline headline-offer">OFFER</h1>
  <div class="headline-dots"><span></span><span></span><span></span></div>

  <p class="tagline tagline-1">We find, fix and prevent mold,</p>
  <p class="tagline tagline-2">odor and allergen problems</p>

  <div class="phone"></div>
  <svg class="phone-icon" viewBox="0 0 56 56" aria-hidden="true">
    <circle cx="28" cy="28" r="28" fill="#FFFFFF"/>
    <path d="M18 13c2-1 4 0 5 2l3 6c1 2 0 3-1 4l-2 2c2 4 5 7 9 9l2-2c1-1 3-2 4-1l6 3c2 1 3 3 2 5l-2 4c-1 2-3 3-6 2-11-3-20-12-23-23-1-3 0-5 2-6z" fill="#000000"/>
  </svg>
  <p class="phone-number">302-555-0148</p>

  <p class="service service-water">Water<br>Damage</p>
  <p class="service service-mold">Mold<br>Services</p>
  <p class="service service-odor">Odor<br>Removal</p>
  <p class="service service-duct">Duct<br>Cleaning</p>
</div>
</body>
</html>
```